Baby prediction and advice cards, thank you notes, Baby shower invitations and diaper raffle tickets

Please see attached brief with description of the project.

*** Only apply if you are DETAIL ORIENTED and willing to read 100% the brief and the correction instructions (if required)***

*** Only apply if you are able to communicate in English 100%***

We need QUALITY over quantity

Contact us if you have questions.

Thank you

Target Market(s)

Expecting mothers and their families (Mothers, sisters)

Font styles to use
Sans Serif

Colors

Designer to choose colors to be used in the design.

Requirements
Must have
• Read the brief
Should not have
• Read the brief

```html
<!DOCTYPE html>
<html lang="en">
<head>
<meta charset="utf-8">
<title>Baby Shower Stationery Set</title>
<link rel="stylesheet" href="https://fonts.googleapis.com/css2?family=Lato:ital,wght@0,400;0,700;1,400&family=Oswald:wght@400;500&family=Allura&display=swap">
<style>
  :root{
    --backdrop:#ebe6e2;
    --paper:#f7f5f3;
    --cocoa:#a57f70;
    --lace:#e3d8d2;
    --ink:#3f3633;
    --rule:#b9aca6;
    --caption:#2e2a28;
  }
  *{box-sizing:border-box;margin:0;padding:0}
  html,body{width:1200px;height:851px;overflow:hidden}
  body{background:var(--backdrop);position:relative;font-family:"Lato",sans-serif;color:var(--ink)}

  .card{position:absolute;background:var(--paper);box-shadow:0 1px 3px rgba(0,0,0,.12)}
  .band{position:absolute;left:0;right:0;background:var(--cocoa)}
  .lace{position:absolute;left:0;right:0;background:linear-gradient(var(--lace),rgba(227,216,210,.25))}
  .lace.bottom{background:linear-gradient(rgba(227,216,210,.25),var(--lace))}

  .prediction{left:71px;top:106px;width:355px;height:496px}
  .signature-page{left:434px;top:106px;width:355px;height:496px}
  .prediction .band.top,.signature-page .band.top{top:12px;height:10px}
  .prediction .lace,.signature-page .lace{top:22px;height:26px}
  .prediction .band.bottom,.signature-page .band.bottom{bottom:0;height:12px}

  .fields{position:absolute;left:24px;right:24px;top:72px}
  .field{display:flex;align-items:flex-end;height:31px;font-size:12px;padding-bottom:11px}
  .field .label{white-space:nowrap;margin-right:8px}
  .field .line{flex:1;border-bottom:1px solid var(--rule);height:1px}
  .choice{display:inline-flex;align-items:center;margin-right:6px}
  .choice::before{content:"";width:11px;height:11px;border:1px solid var(--cocoa);border-radius:50%;margin-right:5px}

  .sign-box{position:absolute;left:81px;top:304px;width:193px;height:47px;border:1px solid var(--lace);border-radius:4px}
  .sign-word{position:absolute;left:0;right:0;top:356px;text-align:center;font-family:"Allura",cursive;font-size:25px;color:var(--cocoa)}

  .invitation{left:827px;top:106px;width:302px;height:425px}
  .invitation .band.top{top:10px;height:9px}
  .invitation .lace.top{top:22px;height:24px}
  .invitation .lace.bottom{top:396px;height:19px}
  .invitation .band.bottom{top:415px;height:10px}
  .celebrating{position:absolute;left:0;right:0;top:82px;text-align:center;font-family:"Oswald",sans-serif;font-weight:500;font-size:18px;letter-spacing:7px;color:var(--cocoa);padding-left:7px}
  .divider{position:absolute;left:79px;width:144px;top:108px;height:12px}
  .headline{position:absolute;left:0;right:0;top:114px;text-align:center;font-family:"Allura",cursive;font-size:42px;color:var(--cocoa);line-height:1}
  .pill{position:absolute;left:58px;top:195px;width:184px;height:26px;border-radius:5px;background:var(--cocoa);color:#fff;font-family:"Oswald",sans-serif;font-size:13px;text-align:center;line-height:26px;letter-spacing:-.2px}
  .invitation .fields{left:21px;right:22px;top:228px}
  .invitation .field{height:29.6px;padding-bottom:9px}
  .invitation .field .line + .label{margin-left:2px}

  .raffle{left:827px;top:581px;width:248px;height:141px}
  .raffle .stripe{position:absolute;left:6px;top:0;bottom:0;width:5px;background:var(--cocoa)}
  .raffle .lace.side{left:14px;right:auto;top:0;bottom:0;width:10px;background:var(--lace)}
  .raffle-title{position:absolute;left:20px;right:0;top:20px;text-align:center;font-family:"Oswald",sans-serif;font-size:16px;color:var(--cocoa);letter-spacing:-.2px}
  .raffle-note{position:absolute;left:39px;top:50px;width:190px;height:44px;border:1px solid var(--lace);border-radius:4px;font-style:italic;font-size:10.5px;text-align:center;line-height:16px;padding-top:5px;color:#5b504c}
  .raffle .fields{left:39px;right:19px;top:104px}
  .raffle .field{font-size:10px;height:20px;padding-bottom:4px}

  .caption{position:absolute;font-size:16px;color:var(--caption);transform:translateX(-50%);white-space:nowrap}
</style>
</head>
<body>

<section class="card prediction">
  <div class="band top"></div>
  <div class="lace top" role="img" aria-label="Lace border trim"></div>
  <div class="fields">
    <div class="field"><span class="label">Baby’s name:</span><span class="line"></span></div>
    <div class="field"><span class="label">Gender:</span><span class="line"></span></div>
    <div class="field"><span class="label">Date of birth:</span><span class="line"></span></div>
    <div class="field"><span class="label">Time of birth:</span><span class="line"></span></div>
    <div class="field"><span class="label">Weight:</span><span class="line"></span></div>
    <div class="field"><span class="label">Length:</span><span class="line"></span></div>
    <div class="field"><span class="label">Hair Color:</span><span class="line"></span></div>
    <div class="field"><span class="label">Eye Color:</span><span class="line"></span></div>
    <div class="field"><span class="label">Resemblance:</span><span class="choice">All dad</span><span class="choice">All mom</span><span class="choice">Both</span></div>
    <div class="field"><span class="label">I hope you get mom’s:</span><span class="line"></span></div>
    <div class="field"><span class="label">I hope you get dad’s:</span><span class="line"></span></div>
    <div class="field"><span class="label">My best advice:</span><span class="line"></span></div>
    <div class="field"><span class="label">Best wishes and love from:</span><span class="line"></span></div>
  </div>
  <div class="band bottom"></div>
</section>

<section class="card signature-page">
  <div class="band top"></div>
  <div class="lace top" role="img" aria-label="Lace border trim"></div>
  <div class="sign-box"></div>
  <div class="sign-word">Signature</div>
  <div class="band bottom"></div>
</section>

<p class="caption" style="left:428px;top:615px">Baby prediction and Advice card</p>

<section class="card invitation">
  <div class="band top"></div>
  <div class="lace top" role="img" aria-label="Lace border trim"></div>
  <div class="celebrating">CELEBRATING</div>
  <svg class="divider" viewBox="0 0 144 12" aria-hidden="true">
    <path d="M0 3 H62 L60 8 H2 Z M82 3 H144 L142 8 H84 Z" fill="#a57f70"/>
    <text x="72" y="10" text-anchor="middle" font-family="Oswald, sans-serif" font-size="9" fill="#a57f70">A</text>
  </svg>
  <div class="headline">Baby on the Way</div>
  <div class="pill">JOIN US FOR A SHOWER HONORING:</div>
  <div class="fields">
    <div class="field"><span class="label">Date:</span><span class="line"></span><span class="label" style="margin-left:2px">Time:</span><span class="line"></span></div>
    <div class="field"><span class="label">Place:</span><span class="line"></span></div>
    <div class="field"><span class="label">Details:</span><span class="line"></span></div>
    <div class="field"><span class="label">RSVP to:</span><span class="line"></span></div>
    <div class="field"><span class="label">Hosted by:</span><span class="line"></span></div>
  </div>
  <div class="lace bottom" role="img" aria-label="Lace border trim"></div>
  <div class="band bottom"></div>
</section>

<p class="caption" style="left:978px;top:540px">Invitation</p>

<section class="card raffle">
  <div class="stripe"></div>
  <div class="lace side" role="img" aria-label="Lace border trim"></div>
  <div class="raffle-title">DIAPER RAFFLE TICKET</div>
  <div class="raffle-note">Bring a pack of diapers (any size)<br>for your chance to win a prize!</div>
  <div class="fields">
    <div class="field"><span class="label">Name:</span><span class="line"></span></div>
  </div>
</section>

<p class="caption" style="left:951px;top:727px">Diaper Raffle ticket:</p>

</body>
</html>
```